Quality Improvement Software for healthcare agencies needs a website.

VORTEL218 is a software for hospices and home health agencies to manage their Quality Assurance Performance Improvement programs to remain complaint with the standards set by Sanavox and the Bureau of Clinical Oversight. The web accessible software-as-a-service provides an easy, turn-key way for agencies to organize all the information they need to manage and track.

Coding

Coded - Design and coding required

Number of Pages Required

4 page

```html
<!DOCTYPE html>
<html lang="en">
<head>
<meta charset="utf-8">
<title>VORTEL218 — Quality Improvement Software</title>
<link href="https://fonts.googleapis.com/css2?family=Rubik:wght@500;700&family=Roboto:wght@400;500;700&family=Great+Vibes&display=swap" rel="stylesheet">
<style>
:root{
  --navy:#1b2d4a;
  --yellow:#fccb06;
  --green:#6cbb12;
  --blue:#27b3f7;
  --orange:#f68b1f;
  --grey-bg:#f4f4f4;
  --text:#777;
  --dark:#111;
  --script:#9fd3f1;
}
*{margin:0;padding:0;box-sizing:border-box}
html,body{width:1200px;height:3553px;overflow:hidden}
body{position:relative;font-family:Roboto,Arial,sans-serif;color:var(--dark);background:#fff}
.abs{position:absolute}
section,header,footer{position:absolute;left:0;width:1200px}

/* Header */
.site-header{top:0;height:101px;background:#fff;border-bottom:1px solid #e6e6e6}
.brand{left:112px;top:30px;display:flex;align-items:center;gap:10px}
.brand-mark{width:34px;height:34px;background:var(--yellow);flex:none}
.brand-name{font-family:Rubik,sans-serif;font-weight:700;font-size:34px;line-height:1;color:var(--navy);letter-spacing:.5px;white-space:nowrap}
.header-divider{left:419px;top:14px;width:2px;height:74px;background:#333}
.main-nav{left:443px;top:42px;display:flex;gap:30px;font-size:14px}
.main-nav a{color:#222;text-decoration:none}
.btn{display:flex;align-items:center;justify-content:center;font-weight:700;font-size:14px;text-transform:uppercase;color:#111;text-decoration:none}
.btn-login{left:847px;top:28px;width:117px;height:44px;border:1px solid #999;background:#fff}
.btn-signin{left:972px;top:28px;width:116px;height:44px;background:var(--yellow)}

/* Hero */
.hero{top:101px;height:600px;overflow:hidden}
.hero-photo{left:0;top:0;width:1200px;height:600px;background:linear-gradient(100deg,#0d1c22 0%,#1d3238 30%,#5a4a35 55%,#8a5a2f 75%,#3a2a1e 100%)}
.hero-copy{left:110px;top:155px;width:456px;text-align:center;color:#fff}
.hero-welcome{font-size:21px}
.hero-title{font-family:Rubik,sans-serif;font-weight:500;font-size:74px;line-height:1.1;margin-top:4px}
.hero-text{font-size:14px;line-height:26px;margin-top:10px}
.btn-start{left:281px;top:400px;width:126px;height:41px;background:var(--yellow)}
.scroll-tab{left:550px;top:563px;width:100px;height:74px;border-radius:50px 50px 0 0;background:#fff}

/* Section headings */
.eyebrow{font-family:"Great Vibes",cursive;font-size:34px;color:var(--script);text-align:center}
.section-title{font-family:Rubik,sans-serif;font-weight:700;font-size:34px;color:var(--navy);text-align:center}
.section-title .accent{color:#a8e06a;-webkit-text-stroke:1px var(--green)}

/* About */
.about{top:701px;height:571px}
.about-visual{left:139px;top:92px;width:366px;height:378px;background:linear-gradient(135deg,#e7edf5 0%,#dce8f0 50%,#eef2e4 100%)}
.about-copy{left:648px;top:120px;width:425px;text-align:center}
.about-text{font-size:13.5px;line-height:25.6px;color:var(--text);margin-top:30px}
.btn-more{left:803px;top:391px;width:115px;height:42px;background:var(--yellow);font-size:13px}

/* Services */
.services{top:1272px;height:594px;background:var(--grey-bg)}
.services-head{left:0;top:30px;width:1200px}
.slider-arrows{display:flex;gap:6px}
.slider-arrows span{width:40px;height:28px;background:var(--navy);display:flex;align-items:center;justify-content:center}
.services .slider-arrows{left:1000px;top:112px}
.connector{stroke:var(--navy);stroke-width:4;fill:none}
.service-card{width:207px}
.service-photo{width:207px}
.service-body{text-align:center;color:#fff;padding:8px 8px 0}
.service-body h3{font-size:15px;font-weight:700;margin:2px 0 6px}
.service-body p{font-size:12.5px;line-height:22.6px}
.card-btn{width:40px;height:27px;background:var(--navy);display:flex;align-items:center;justify-content:center}
.tone-blue{background:var(--blue)}
.tone-green{background:var(--green)}
.tone-orange{background:var(--orange)}
.tone-yellow{background:var(--yellow)}

/* Testimonials */
.testimonials{top:1866px;height:661px;background:#fff}
.testimonials .slider-arrows{left:1000px;top:238px}
.client-photo{left:134px;top:306px;width:310px;height:310px;border-radius:50%;background:radial-gradient(circle at 50% 40%,#dfe7ec 0%,#b9c8d2 55%,#1f2f55 56%,#223460 100%)}
.quote-card{top:280px;width:294px;height:299px;background:#fff;border:2px solid #eee;padding:18px 16px}
.quote-card p{font-size:13.5px;line-height:25.6px;color:#8a8a8a}
.quote-mark{margin-top:8px}
.quote-name{font-family:"Great Vibes",cursive;color:var(--green);font-size:26px;line-height:1;margin-top:6px}
.quote-role{font-family:"Great Vibes",cursive;color:var(--green);font-size:16px}

/* Contact */
.contact{top:2527px;height:663px;background:var(--grey-bg)}
.contact-frame{left:119px;top:114px;width:326px;height:459px;background:var(--orange)}
.contact-photo{left:110px;top:122px;width:327px;height:459px;background:radial-gradient(circle at 50% 45%,#1f3f68 0%,#0f2240 55%,#081427 100%)}
.contact-form{left:499px;top:190px;width:315px;height:240px}
.field-label{display:block;font-size:11px;color:#555}
.field-line{width:315px;height:1px;background:#999}
.btn-submit{left:499px;top:463px;width:116px;height:41px;background:var(--yellow);font-size:13px}
.info-box{left:841px;top:162px;width:249px;height:360px;border:1px solid #333;background:var(--grey-bg)}
.info-row{position:absolute;left:0;width:249px;padding-left:50px;font-size:14px;color:#222}
.info-row .label{display:flex;align-items:center;gap:6px;text-transform:uppercase}
.info-row .value{margin-top:10px}
.info-sep{position:absolute;left:0;width:249px;height:1px;background:#333}

/* Footer */
.site-footer{top:3190px;height:363px;background:#000;color:#fff}
.footer-brand{left:112px;top:60px;display:flex;align-items:center;gap:14px}
.footer-brand .brand-mark{width:48px;height:48px}
.footer-brand .brand-name{color:#fff;font-size:54px;letter-spacing:1px}
.footer-about{left:112px;top:150px;width:405px;font-size:12.5px;line-height:25.6px}
.footer-col{top:90px}
.footer-col h4{font-family:Rubik,sans-serif;font-weight:500;font-size:21px;margin-bottom:18px}
.footer-col ul{list-style:none}
.footer-col li{font-size:14px;height:41px;display:flex;align-items:center;gap:8px}
.dot{width:10px;height:10px;border-radius:50%;background:var(--orange);display:inline-block}
.copyright{left:0;top:317px;width:1200px;text-align:center;font-size:10px}
</style>
</head>
<body>

<header class="site-header">
  <div class="abs brand"><span class="brand-mark"></span><span class="brand-name">VORTEL218</span></div>
  <div class="abs header-divider"></div>
  <nav class="abs main-nav"><a href="#">Home</a><a href="#">About Us</a><a href="#">Services</a><a href="#">Testimonials</a></nav>
  <a class="abs btn btn-login" href="#">Log In</a>
  <a class="abs btn btn-signin" href="#">Sign In</a>
</header>

<section class="hero">
  <div class="abs hero-photo" role="img" aria-label="Two colleagues studying data on a glowing screen in a dim office"></div>
  <div class="abs hero-copy">
    <div class="hero-welcome">Welcome To</div>
    <h1 class="hero-title">Vortel218</h1>
    <p class="hero-text">Lorem ipsum dolor sit amet, consectetur adipiscing elit, sed do eiusmod tempor incididunt ut labore et dolore magna aliqua. Quis ipsum suspendisse ultrices gravida. Risus commodo viverra maecenas accumsan lacus vel facilisis.</p>
  </div>
  <a class="abs btn btn-start" href="#">Get Started</a>
  <div class="abs scroll-tab">
    <svg class="abs" style="left:43px;top:32px" width="14" height="9" viewBox="0 0 14 9"><path d="M1 1l6 6 6-6" stroke="var(--orange)" stroke-width="2" fill="none"/></svg>
  </div>
</section>

<section class="about">
  <div class="abs about-visual" role="img" aria-label="Illustration of a rising growth chart in blue, green, orange and yellow"></div>
  <div class="abs about-copy">
    <div class="eyebrow">Who We Are</div>
    <h2 class="section-title">About <span class="accent">Us</span></h2>
    <p class="about-text">VORTEL218 is a software for hospices and home health agencies to manage their Quality Assurance Performance Improvement programs to remain compliant with the standards set by Sanavox and the Bureau of Clinical Oversight. The web accessible software-as-a-service provides an easy, turn-key way for agencies to organize all the information they need to manage and track.</p>
  </div>
  <a class="abs btn btn-more" href="#">Read More</a>
</section>

<section class="services">
  <div class="abs services-head">
    <div class="eyebrow">What We Do</div>
    <h2 class="section-title">Our <span class="accent">Services</span></h2>
  </div>
  <div class="abs slider-arrows">
    <span><svg width="18" height="8" viewBox="0 0 18 8"><path d="M17 4H2M5 1L1 4l4 3" stroke="var(--yellow)" stroke-width="2" fill="none"/></svg></span>
    <span><svg width="18" height="8" viewBox="0 0 18 8"><path d="M1 4h15M13 1l4 3-4 3" stroke="var(--yellow)" stroke-width="2" fill="none"/></svg></span>
  </div>
  <svg class="abs" style="left:0;top:0" width="1200" height="594">
    <path class="connector" d="M319 206L368 172M575 172L625 206M832 206L881 148"/>
  </svg>

  <article class="abs service-card" style="left:112px;top:206px">
    <div class="service-photo" style="height:118px;background:linear-gradient(135deg,#3a4650,#9aa6ae)" role="img" aria-label="Developer working at a multi-monitor desk"></div>
    <div class="service-body tone-blue" style="height:196px;margin-top:4px"><h3>Lorem Ipsum</h3><p>Lorem ipsum dolor sit amet, consectetur adipiscing elit, sed do eiusmod tempor incididunt ut labore et dolore magna aliqua. Quis ipsum suspendisse ultrices gravida.</p></div>
  </article>
  <article class="abs service-card" style="left:368px;top:172px">
    <div class="service-photo" style="height:117px;background:linear-gradient(135deg,#6b4a2c,#c8b9a6)" role="img" aria-label="Team collaborating around a laptop"></div>
    <div class="service-body tone-green" style="height:231px;margin-top:4px"><h3>Lorem Ipsum</h3><p>Lorem ipsum dolor sit amet, consectetur adipiscing elit, sed do eiusmod tempor incididunt ut labore et dolore magna aliqua. Quis ipsum suspendisse ultrices gravida.suspendisse ultrices gravida.</p></div>
  </article>
  <article class="abs service-card" style="left:625px;top:206px">
    <div class="service-photo" style="height:118px;background:linear-gradient(135deg,#5a6670,#c9a27a)" role="img" aria-label="Colleagues reviewing work on a monitor"></div>
    <div class="service-body tone-orange" style="height:196px;margin-top:4px"><h3>Lorem Ipsum</h3><p>Lorem ipsum dolor sit amet, consectetur adipiscing elit, sed do eiusmod tempor incididunt ut labore et dolore magna aliqua. Quis ipsum suspendisse ultrices gravida.</p></div>
  </article>
  <article class="abs service-card" style="left:881px;top:148px">
    <div class="service-photo" style="height:118px;background:linear-gradient(135deg,#1e3448,#6f8ea8)" role="img" aria-label="Professionals using tablets with digital interface overlay"></div>
    <div class="service-body tone-yellow" style="height:253px;margin-top:5px"><h3>Lorem Ipsum</h3><p>Lorem ipsum dolor sit amet, consectetur adipiscing elit, sed do eiusmod tempor incididunt ut labore et dolore magna aliqua. Quis ipsum suspendisse ultrices gravida.suspendisse ultrices gravida.suspendisse ultrices gravida.</p></div>
  </article>

  <a class="abs card-btn" style="left:193px;top:510px" href="#"><svg width="7" height="10" viewBox="0 0 7 10"><path d="M1 1l4 4-4 4" stroke="var(--yellow)" stroke-width="2" fill="none"/></svg></a>
  <a class="abs card-btn" style="left:449px;top:510px" href="#"><svg width="7" height="10" viewBox="0 0 7 10"><path d="M1 1l4 4-4 4" stroke="var(--yellow)" stroke-width="2" fill="none"/></svg></a>
  <a class="abs card-btn" style="left:706px;top:510px" href="#"><svg width="7" height="10" viewBox="0 0 7 10"><path d="M1 1l4 4-4 4" stroke="var(--yellow)" stroke-width="2" fill="none"/></svg></a>
  <a class="abs card-btn" style="left:963px;top:510px" href="#"><svg width="7" height="10" viewBox="0 0 7 10"><path d="M1 1l4 4-4 4" stroke="var(--yellow)" stroke-width="2" fill="none"/></svg></a>
</section>

<section class="testimonials">
  <div class="abs" style="left:0;top:90px;width:1200px">
    <div class="eyebrow">Our Testimonials</div>
    <h2 class="section-title">What Our Claints <span class="accent">Says</span></h2>
  </div>
  <div class="abs slider-arrows">
    <span><svg width="18" height="8" viewBox="0 0 18 8"><path d="M17 4H2M5 1L1 4l4 3" stroke="var(--yellow)" stroke-width="2" fill="none"/></svg></span>
    <span><svg width="18" height="8" viewBox="0 0 18 8"><path d="M1 4h15M13 1l4 3-4 3" stroke="var(--yellow)" stroke-width="2" fill="none"/></svg></span>
  </div>
  <div class="abs client-photo" role="img" aria-label="Portrait of a smiling client in a navy suit, arms crossed"></div>

  <blockquote class="abs quote-card" style="left:490px">
    <p>Lorem ipsum dolor sit amet, piscing elit, d do eiusmod tempor incididunt ut labore et dolore magna aliqua. Quis ipsum pendisse accumsan lacus vel facilisis. Lorem lor sit amet, consectetur adipiscing elit, sed doe mod tempor incididunt ut labore remagna aliqua facilisis.</p>
    <svg class="quote-mark" width="18" height="14" viewBox="0 0 18 14"><path d="M0 0h7v7L4 14H1l2-7H0zM10 0h7v7l-3 7h-3l2-7h-3z" fill="var(--green)"/></svg>
    <div class="quote-name">Ray Holden</div>
    <div class="quote-role">Lorem Ipsum</div>
  </blockquote>
  <blockquote class="abs quote-card" style="left:794px">
    <p>Lorem ipsum dolor sit amet, piscing elit, d do eiusmod tempor incididunt ut labore et dolore magna aliqua. Quis ipsum pendisse accumsan lacus vel facilisis. Lorem lor sit amet, consectetur adipiscing elit, sed doe mod tempor incididunt ut labore remagna aliqua facilisis.</p>
    <svg class="quote-mark" width="18" height="14" viewBox="0 0 18 14"><path d="M0 0h7v7L4 14H1l2-7H0zM10 0h7v7l-3 7h-3l2-7h-3z" fill="var(--green)"/></svg>
    <div class="quote-name">Ray Holden</div>
    <div class="quote-role">Lorem Ipsum</div>
  </blockquote>
</section>

<section class="contact">
  <div class="abs" style="left:0;top:30px;width:1200px">
    <div class="eyebrow">Speak To Us</div>
    <h2 class="section-title">Contact <span class="accent">Us</span></h2>
  </div>
  <div class="abs contact-frame"></div>
  <div class="abs contact-photo" role="img" aria-label="Hand pointing up at floating contact icons on a dark blue background"></div>

  <form class="abs contact-form">
    <label class="abs field-label" style="top:0">Full Name</label>
    <div class="abs field-line" style="top:52px"></div>
    <label class="abs field-label" style="top:91px">Email</label>
    <div class="abs field-line" style="top:134px"></div>
    <label class="abs field-label" style="top:186px">Teaxt Here</label>
    <div class="abs field-line" style="top:234px"></div>
  </form>
  <a class="abs btn btn-submit" href="#">Submit</a>

  <div class="abs info-box">
    <div class="info-row" style="top:34px">
      <div class="label"><svg width="13" height="10" viewBox="0 0 13 10"><rect x="0.5" y="0.5" width="12" height="9" fill="var(--orange)"/><path d="M1 1l5.5 4.5L12 1" stroke="#fff" fill="none"/></svg> Email Us</div>
      <div class="value" style="padding-left:19px">info@vortel218.com</div>
    </div>
    <div class="info-sep" style="top:117px"></div>
    <div class="info-row" style="top:156px">
      <div class="label"><svg width="10" height="14" viewBox="0 0 10 14"><path d="M5 0a5 5 0 015 5c0 4-5 9-5 9S0 9 0 5a5 5 0 015-5z" fill="var(--orange)"/><circle cx="5" cy="5" r="2" fill="#fff"/></svg> Located In</div>
      <div class="value" style="padding-left:16px">Lorem Ipsum,USA</div>
    </div>
    <div class="info-sep" style="top:239px"></div>
    <div class="info-row" style="top:274px">
      <div class="label"><svg width="12" height="12" viewBox="0 0 12 12"><path d="M2 0l3 3-1.5 2A7 7 0 007 8.5L9 7l3 3-2 2C4 12 0 8 0 2z" fill="var(--orange)"/></svg> Call Us</div>
      <div class="value" style="padding-left:18px">+1 888 888 8888</div>
    </div>
  </div>
</section>

<footer class="site-footer">
  <div class="abs footer-brand"><span class="brand-mark"></span><span class="brand-name">VORTEL218</span></div>
  <p class="abs footer-about">Lorem ipsum dolor sit amet, consectetur adipiscing elit, sed do smod tempor incididunt ut labore et dolore magna aliqua. Quis ipsum disse ultrices gravida. Risus commodo viverra maecenas accumsan lacus vel facilisis.disse ultrices gravida. Risus commodo viverra cumsan lacus el facilisis.</p>

  <div class="abs footer-col" style="left:583px">
    <h4>Quick Lins</h4>
    <ul><li>Home</li><li>About Us</li><li>Services</li><li>Testimonials</li></ul>
  </div>
  <div class="abs footer-col" style="left:742px">
    <h4>Contact Us</h4>
    <ul>
      <li><svg width="13" height="10" viewBox="0 0 13 10"><rect x="0.5" y="0.5" width="12" height="9" stroke="var(--orange)" fill="none"/><path d="M1 1l5.5 4.5L12 1" stroke="var(--orange)" fill="none"/></svg>info@vortel218.com</li>
      <li><svg width="12" height="12" viewBox="0 0 12 12"><path d="M2 0l3 3-1.5 2A7 7 0 007 8.5L9 7l3 3-2 2C4 12 0 8 0 2z" fill="var(--orange)"/></svg>+1 888 888 8888</li>
      <li><svg width="10" height="14" viewBox="0 0 10 14"><path d="M5 0a5 5 0 015 5c0 4-5 9-5 9S0 9 0 5a5 5 0 015-5z" fill="var(--orange)"/><circle cx="5" cy="5" r="2" fill="#000"/></svg>Lorem Ipsum,USA</li>
    </ul>
  </div>
  <div class="abs footer-col" style="left:975px">
    <h4>Social Media</h4>
    <ul><li><span class="dot"></span>Friendwall</li><li><span class="dot"></span>Chirpline</li><li><span class="dot"></span>Workround</li><li><span class="dot"></span>Snapgrid</li></ul>
  </div>
  <div class="abs copyright">© 2023 Vortel218 | All Rights Reserved</div>
</footer>

</body>
</html>
```